Ward Compass Business Card Design*

We need a business card design for our company Ward Compass. Our company is specialized in providing online consulting services regarding medical institutions, hospitals and doctors. We work with patients worldwide looking to choose between healthcare providers. We have a website you may use as a reference, where we list doctors and clinics worldwide. So we target Medical providers as well as patients worldwide.
Target Market(s)
Medical Providers and patients around the world
Industry/Entity Type
Medical
Contact Information for Business Card
Salma Derkaoui
CEO
+90 612 348 2071
info@wardcompass-example.com
www.wardcompass-example.com
14 Annakhil 3 H.R.B. Rabat, Morocco
Requirements
Must have
- Company logo/name on one full side, personal info and smaller logo and company name on the other side.
Nice to have
- Smart and elegant design

```html
<!DOCTYPE html>
<html lang="en">
<head>
<meta charset="utf-8">
<title>Ward Compass – Business Card</title>
<link href="https://fonts.googleapis.com/css2?family=Open+Sans:wght@300;400;600;700&display=swap" rel="stylesheet">
<style>
  :root{
    --stage:#e7e4df;
    --navy:#0f4c8a;
    --navy-deep:#0a3a6e;
    --navy-light:#1763a6;
    --grey:#a7a9ac;
    --grey-light:#c9cacc;
    --paper:#ffffff;
    --paper-shade:#eef0f2;
    --ink-light:#ffffff;
    --glow:rgba(255,255,255,.07);
  }
  *{margin:0;padding:0;box-sizing:border-box}
  html,body{width:1200px;height:780px;overflow:hidden;background:var(--stage);
    font-family:"Open Sans",Arial,sans-serif}
  .stage{position:relative;width:1200px;height:780px}

  .card{position:absolute;top:240px;width:520px;height:300px;border-radius:16px;overflow:hidden;
    box-shadow:0 10px 28px rgba(0,0,0,.22),0 2px 6px rgba(0,0,0,.12)}
  .card-front{left:60px;background:linear-gradient(135deg,var(--paper) 40%,var(--paper-shade))}
  .card-back{left:620px;
    background:radial-gradient(circle at 50% 48%,var(--navy-light) 0%,var(--navy) 45%,var(--navy-deep) 100%)}

  .front-shapes{position:absolute;inset:0;width:520px;height:300px}

  .brand{position:absolute;display:flex;align-items:center;gap:12px;white-space:nowrap}
  .brand-front{left:34px;top:74px}
  .brand-dot{display:block;border-radius:50%;flex:none}
  .brand-front .brand-dot{width:30px;height:30px;border:5px solid var(--navy)}
  .brand-name{font-weight:700;letter-spacing:1px;text-transform:uppercase}
  .brand-front .brand-name{color:var(--navy);font-size:22px}

  .website{position:absolute;right:24px;top:122px;color:var(--ink-light);font-size:11px;letter-spacing:.3px;white-space:nowrap}

  .person{position:absolute;left:232px;top:188px;color:var(--ink-light)}
  .person-name{font-size:15px;font-weight:700;text-transform:uppercase;letter-spacing:.4px}
  .person-role{font-size:11px;font-weight:300;letter-spacing:.6px;margin-top:1px}
  .contact{list-style:none;margin-top:12px;font-size:11px}
  .contact li{display:flex;align-items:center;gap:8px;margin-top:4px}
  .contact svg{width:10px;height:10px;flex:none}

  .back-glow{position:absolute;left:50%;top:48%;width:340px;height:340px;transform:translate(-50%,-50%);
    border-radius:50%;background:radial-gradient(circle,var(--glow) 0%,var(--glow) 40%,transparent 70%)}

  .brand-back{left:50%;top:50%;transform:translate(-50%,-50%)}
  .brand-back .brand-dot{width:40px;height:40px;border:6px solid var(--ink-light)}
  .brand-back .brand-name{color:var(--ink-light);font-size:30px}
</style>
</head>
<body>
<main class="stage">
  <section class="card card-front" aria-label="Card front">
    <svg class="front-shapes" viewBox="0 0 520 300" aria-hidden="true">
      <defs>
        <linearGradient id="bandGrey" x1="0" y1="0" x2="1" y2="0">
          <stop offset="0" stop-color="var(--grey-light)"/>
          <stop offset="1" stop-color="var(--grey)"/>
        </linearGradient>
        <linearGradient id="fieldBlue" x1="0" y1="1" x2="1" y2="0">
          <stop offset="0" stop-color="var(--navy-deep)"/>
          <stop offset=".5" stop-color="var(--navy-light)"/>
          <stop offset="1" stop-color="var(--navy)"/>
        </linearGradient>
      </defs>
      <path class="wave-band" d="M58,300 C120,236 172,166 276,112 C370,64 446,50 520,46 L520,300 Z" fill="url(#bandGrey)"/>
      <path class="wave-field" d="M80,300 C140,240 190,175 290,125 C380,80 450,68 520,64 L520,300 Z"
            fill="url(#fieldBlue)" stroke="var(--paper)" stroke-width="3"/>
    </svg>

    <div class="brand brand-front">
      <span class="brand-dot"></span>
      <span class="brand-name">Ward Compass</span>
    </div>

    <p class="website">www.wardcompass-example.com</p>

    <div class="person">
      <p class="person-name">Salma Derkaoui</p>
      <p class="person-role">CEO</p>
      <ul class="contact">
        <li>
          <svg viewBox="0 0 10 10" aria-hidden="true"><rect x="2.5" y=".5" width="5" height="9" rx="1" fill="none" stroke="currentColor" stroke-width="1"/></svg>
          <span>+90 612 348 2071</span>
        </li>
        <li>
          <svg viewBox="0 0 10 10" aria-hidden="true"><rect x=".5" y="1.5" width="9" height="7" fill="none" stroke="currentColor" stroke-width="1"/><path d="M.5,1.5 L5,5.5 L9.5,1.5" fill="none" stroke="currentColor" stroke-width="1"/></svg>
          <span>info@wardcompass-example.com</span>
        </li>
      </ul>
    </div>
  </section>

  <section class="card card-back" aria-label="Card back">
    <div class="back-glow" role="img" aria-label="Soft light glow behind the company name"></div>
    <div class="brand brand-back">
      <span class="brand-dot"></span>
      <span class="brand-name">Ward Compass</span>
    </div>
  </section>
</main>
</body>
</html>
```